Design a Bold Tradeshow Backdrop for a Sustainable Cleaning Technology

We need a professional, high-impact 10' × 8' tradeshow backdrop for Vornelle®, a commercial cleaning technology company. 143.75" x 90" high and needs bleeds in the 143.75" direction for printing but the graphic area is 10' wide.

Our first event will have an audience that includes K–12 school administrators, facility managers, business officials, and custodial decision-makers. However, this backdrop will be used at multiple future trade shows across different commercial and institutional markets.

The design therefore needs to be universal rather than specifically education- or school-themed.

Our goal is to stop attendees as they walk past the booth and immediately communicate a simple message:

Safer and more sustainable cleaning can also cost substantially less than conventional cleaning chemicals.

We want the design to feel modern, innovative, clean, sustainable, credible, commercial, and premium. It should resonate with K–12 decision-makers while being equally appropriate at events serving commercial facilities, healthcare, hospitality, government, property management, transportation, and other institutional markets.

It should NOT look like a traditional janitorial supply advertisement and should not be overly busy.

The most important messages need to be understandable from approximately 10–20 feet away.

Required Messaging

The primary headline should be:

SUSTAINABLE CLEANING
DOES NOT HAVE TO BE EXPENSIVE.

Three major value propositions should be prominently displayed:

FREE
Cleaning Chemical Analysis
See how much you can save.

SAVE UP TO 60% or More
on Cleaning Chemical Costs

AS LITTLE AS $0.27/GALLON

We would also like a strong secondary message incorporated into the design:

SMARTER CLEANING.
High Performance. Low Cost. Safer.

Visual Direction — Important

Rather than showing a K–12 school hallway or other environment that limits the backdrop to the education market, we want a sophisticated, universal commercial or institutional environment.

This could be a bright, contemporary commercial facility, lobby, corridor, office environment, public building, or other premium architectural space that could reasonably represent many different types of facilities.

The environment should communicate:

Cleanliness • Safety • Sustainability • Professionalism • Efficiency • High Performance

We want someone from a school, hospital, hotel, office building, airport, government facility, or other commercial property to be able to look at the backdrop and relate the imagery to their own facility.

Please avoid imagery that makes the backdrop industry-specific.

We also want to avoid clichéd environmental imagery. The design does not need to be covered in leaves, trees, water droplets, recycling symbols, or other obvious "green" graphics to communicate sustainability. We prefer a sophisticated commercial interpretation of sustainability.

Color & Brand Direction

We want the overall color palette to stay primarily within:

Blues — consistent with our corporate identity

Greens — to reinforce sustainability, safety, efficiency, and environmental responsibility

White — strongly encouraged for clean space, contrast, and an open contemporary appearance

Black — should be limited primarily to text where necessary for readability

Please avoid making black a major background or dominant design color.

We want the finished display to have a bright, clean, sophisticated, sustainable look and feel rather than a dark or industrial appearance.

The design should use significant negative space and a strong visual hierarchy.

Less is more.

We prefer a few large, powerful messages that can be understood quickly rather than numerous small bullet points, paragraphs, or icons.

Creative Freedom

The attached concept image is provided to communicate our general direction and messaging only.

It does not need to be copied.

We are specifically running this contest because we want designers to improve upon our initial concept and show us different creative approaches to presenting the Vornelle value proposition.

We are open to creative interpretations of the commercial environment, composition, typography, use of negative space, and how the three major financial benefits are presented.

The finished design should feel like an innovative commercial technology brand, not simply another cleaning chemical company.

Corporate Logo — Very Important

We are attaching our official Vornelle® corporate logo for use in the design.

DO NOT redraw, recreate, modify, stylize, reinterpret, trace, or AI-generate the Vornelle logo.

The supplied corporate logo must be inserted directly into the artwork exactly as provided, maintaining its original proportions, colors, typography, trademark elements, and graphic design.

The logo should generally appear in the upper-left area of the backdrop but should not overwhelm the primary marketing message.

Printer Template & Graphic Sizing

We are also attaching the printer's official graphic template and instructions for the 8' × 8' tension-fabric display.

Designers should create their artwork using these supplied specifications so the winning design can be transferred directly into production.

The printer requires that the original document size not be changed, artwork be created on the designated design layer or a new layer, images be embedded, text be converted to outlines, and the finished production artwork be supplied as a PDF.

Please pay particular attention to the bleed area, finished size, and safe artwork area when positioning important text, graphics, and the corporate logo.

Physical Booth Context

The backdrop will sit behind an 8' tradeshow table.

The complete booth will also contain:

A blue stretch tablecloth with the Vornelle corporate logo
BrevoMax and Vornelle product containers and samples on the table
An HulaDrent chemical mixing/dilution station displayed on an elevated stand to the left
A television/monitor to the right demonstrating our online ROI cost-savings calculator

Because these other booth elements will explain our products and technology in greater detail, the backdrop should NOT attempt to explain everything we do.

Its primary purpose is to stop traffic, establish the Vornelle brand, and communicate our core economic and sustainability value proposition.

Final Deliverables

The winning designer must provide artwork properly sized and positioned using our supplied 8' × 8' tension-fabric display template.

Final files should include:

Print-ready, high-resolution PDF
Editable source/vector artwork
All images embedded
Fonts converted to outlines
Artwork correctly positioned within the supplied printer template
Original Vornelle corporate logo incorporated without modification
The 3–5 Second Test

This is perhaps the most important requirement.

Someone walking down a tradeshow aisle should be able to look at the backdrop for 3–5 seconds and understand:

Vornelle offers safer, sustainable, high-performance commercial cleaning — at a lower cost.

The three offers we particularly want them to remember are:

FREE CHEMICAL ANALYSIS

SAVE UP TO 60%

AS LITTLE AS $0.27/GALLON

The overall takeaway should be:

Sustainable cleaning does not have to cost more.

We want the winning design to make that message immediately understandable, credible, and memorable.

Colors
0054AA
0677BA
7BADD7
CADEEF
E8F1F8
0094D4
00A9DD
6FCCEA
C7EBF8
E9F6FB
00AB8E
00BBA5
67D7C9
C6EFE9
E9F9F6
59FF00
82FF00
B8FF75
E3FFCB
F4FFEA

```html
<!DOCTYPE html>
<html lang="en">
<head>
<meta charset="utf-8">
<title>Vornelle® – 10′ × 8′ Tension Fabric Backdrop</title>
<link rel="stylesheet" href="https://fonts.googleapis.com/css2?family=Montserrat:wght@600;700;800&family=Roboto:wght@400&display=swap">
<style>
  :root {
    --blue-deep: #0054AA;
    --blue-mid: #0677BA;
    --blue-sky: #0094D4;
    --blue-mist: #E9F6FB;
    --green: #4CAF50;
    --green-dark: #2E8B3A;
    --ink: #0A0A0A;
    --white: #FFFFFF;
    --template-gray: #666666;
    --caption-gray: #D6D6D6;
  }
  html, body {
    margin: 0;
    padding: 0;
    width: 1200px;
    height: 1200px;
    overflow: hidden;
    background: var(--template-gray);
  }
  .backdrop { display: block; width: 1200px; height: 1200px; }
  .sans { font-family: 'Montserrat', sans-serif; }
  .headline { font-weight: 800; font-size: 44px; }
  .headline-blue { fill: var(--blue-mid); }
  .headline-ink { fill: var(--ink); }
  .headline-green { fill: var(--green-dark); }
  .brand-name { font-family: 'Montserrat', sans-serif; font-weight: 800; font-size: 42px; fill: var(--white); }
  .offer-free { font-weight: 800; font-size: 58px; fill: var(--blue-deep); }
  .offer-ink { font-weight: 700; fill: var(--ink); }
  .offer-white { font-weight: 800; fill: var(--white); }
  .dollar-mark { font-weight: 800; font-size: 140px; fill: var(--green); stroke: var(--white); stroke-width: 5px; paint-order: stroke; }
  .tagline { font-weight: 800; font-size: 48px; fill: var(--ink); }
  .subline { font-weight: 700; font-size: 36px; fill: var(--ink); }
  .caption { font-family: 'Roboto', sans-serif; font-size: 20px; fill: #222; }
</style>
</head>
<body>
<svg class="backdrop" viewBox="0 0 1200 1200" xmlns="http://www.w3.org/2000/svg">
  <defs>
    <linearGradient id="rowGradient" x1="0" y1="0" x2="1" y2="0">
      <stop offset="0" stop-color="#1565B8"/>
      <stop offset="0.45" stop-color="#1E8C9A"/>
      <stop offset="1" stop-color="#4CB050"/>
    </linearGradient>
    <linearGradient id="headlineBar" x1="0" y1="0" x2="1" y2="0">
      <stop offset="0" stop-color="#4CAF50" stop-opacity="0"/>
      <stop offset="1" stop-color="#4CAF50"/>
    </linearGradient>
    <linearGradient id="panelBlue" x1="0" y1="0" x2="1" y2="1">
      <stop offset="0" stop-color="#0F6DB8"/>
      <stop offset="1" stop-color="#0A7CC4"/>
    </linearGradient>
    <linearGradient id="lobbyTone" x1="0" y1="0" x2="1" y2="1">
      <stop offset="0" stop-color="#DCE6EC"/>
      <stop offset="0.5" stop-color="#F3F6F8"/>
      <stop offset="1" stop-color="#A9B7C2"/>
    </linearGradient>
    <linearGradient id="flaskBadge" x1="0" y1="0" x2="1" y2="1">
      <stop offset="0" stop-color="#0677BA"/>
      <stop offset="1" stop-color="#4CAF50"/>
    </linearGradient>
  </defs>

  <!-- artwork sheet: 143.75 × 90 with side bleed -->
  <rect class="sheet" x="26" y="240" width="1148" height="719" fill="var(--white)" stroke="#222" stroke-width="1"/>

  <!-- logo panel -->
  <polygon points="26,240 440,240 410,440 26,440" fill="url(#panelBlue)"/>
  <polygon points="440,240 474,240 462,300 430,300" fill="var(--green)"/>
  <rect x="132" y="318" width="16" height="16" fill="var(--white)"/>
  <text class="brand-name" x="156" y="354">Vornelle®</text>

  <!-- headline -->
  <g class="sans headline">
    <text class="headline-blue" x="462" y="312">SUSTAINABLE CLEANING</text>
    <text class="headline-ink" x="460" y="366">DOES <tspan class="headline-green">NOT</tspan> HAVE TO BE</text>
    <text class="headline-ink" x="460" y="420">EXPENSIVE.</text>
  </g>
  <rect x="760" y="386" width="316" height="35" fill="url(#headlineBar)"/>

  <!-- facility photograph area -->
  <polygon role="img" aria-label="Bright modern commercial lobby with glass walls, white columns and polished floor"
           points="760,440 1174,440 1174,820 776,820 688,700 654,578" fill="url(#lobbyTone)"/>

  <!-- offer 1: free analysis -->
  <polygon points="26,440 650,440 590,575 26,575" fill="var(--blue-mist)"/>
  <polygon points="650,440 760,440 660,575 590,575" fill="var(--green)"/>
  <circle cx="566" cy="506" r="44" fill="url(#flaskBadge)"/>
  <g class="flask-icon" fill="none" stroke="var(--white)" stroke-width="4" stroke-linejoin="round">
    <path d="M557,478 h18 M560,478 v17 l-18,30 h46 l-18,-30 v-17"/>
    <circle cx="562" cy="512" r="2.5" fill="var(--white)"/>
    <circle cx="572" cy="517" r="2.5" fill="var(--white)"/>
  </g>
  <g class="sans">
    <text class="offer-free" x="132" y="502">FREE</text>
    <text class="offer-ink" x="318" y="500" font-size="32">Cleaning</text>
    <text class="offer-ink" x="132" y="539" font-size="33">Chemical Analysis</text>
    <text class="offer-ink" x="132" y="565" font-size="21">See how much you can save.</text>
  </g>

  <!-- offer 2: savings -->
  <polygon points="26,583 652,583 677,700 26,700" fill="url(#rowGradient)"/>
  <circle cx="630" cy="641" r="44" fill="var(--green)"/>
  <circle cx="630" cy="641" r="38" fill="#050505"/>
  <text class="sans offer-white" x="630" y="659" font-size="50" text-anchor="middle">%</text>
  <g class="sans">
    <text class="offer-white" x="132" y="634" font-size="50">SAVE <tspan font-size="36">UP TO</tspan></text>
    <text class="offer-white" x="130" y="691" font-size="62">60%</text>
    <text class="offer-ink" x="290" y="664" font-size="23">or More on Cleaning</text>
    <text class="offer-ink" x="290" y="691" font-size="23">Chemical Costs</text>
  </g>

  <!-- offer 3: price per gallon -->
  <polygon points="26,708 680,708 770,820 26,820" fill="url(#rowGradient)"/>
  <text class="sans dollar-mark" x="124" y="810">$</text>
  <g class="sans">
    <text class="offer-white" x="230" y="750" font-size="30">AS LITTLE AS</text>
    <text class="offer-white" x="228" y="804" font-size="50">$0.27/GALLON</text>
  </g>

  <!-- secondary message -->
  <g class="sans" text-anchor="middle">
    <text class="tagline" x="600" y="870">SMARTER CLEANING.</text>
    <text class="subline" x="600" y="913">High Performance. Low Cost. Safer.</text>
  </g>

  <!-- footer bands -->
  <rect x="26" y="940" width="1148" height="14" fill="var(--blue-mid)"/>
  <polygon points="890,926 1174,926 1174,954 882,954" fill="var(--green)"/>

  <!-- template guides: 10′ graphic area inside bleed -->
  <g class="safe-guides" fill="none" stroke="#4AB3E0" stroke-width="1" stroke-dasharray="4 4">
    <line x1="121" y1="264" x2="121" y2="936"/>
    <line x1="1079" y1="264" x2="1079" y2="936"/>
    <line x1="121" y1="264" x2="1079" y2="264"/>
  </g>
  <g class="crop-marks" stroke="#DDD" stroke-width="1">
    <line x1="0" y1="264" x2="26" y2="264"/>
    <line x1="121" y1="215" x2="121" y2="240"/>
    <line x1="1079" y1="215" x2="1079" y2="240"/>
    <line x1="1174" y1="264" x2="1200" y2="264"/>
  </g>

  <!-- production caption -->
  <rect x="55" y="972" width="1091" height="36" rx="8" fill="var(--caption-gray)"/>
  <text class="caption" x="600" y="997" text-anchor="middle">Printed Tension Fabric - Final Production Artwork - 10′ × 8′ with Bleed Area</text>
</svg>
</body>
</html>
```